TV - business card

Tidewell Vantage is an insurance brokerage firm, inovative, proactive, vigorous, which aims to become the leader of the insurance brokers in Anfrica. We should like to get some designs which should be avoided also in Gray / Metallic for the Administration and Orange / Blue for the Managers (ike in the picture sent). The Blue / Green logo is not the correct one, but the source of the file. Please adjust the color accordingly for the business cards. 1 / Orange / Blue 2 / Gray / Metallic We want something classic but which is transmitted strenght, inovation, modernity and most of all, rapidity. We want something start-up like, very punchy and catching eye remaining profesional at the same time. Name: Delton Ashgrove Function: Managing Director Address: N ° 73/74 Cmt. Bolembe - R / C 2B Esquerda - Bairro Quimbuta - Luanda Tel: (+244) 947 385 619 Email: delton.ashgrove@tidewell-v.com Website: www.tidewell-v. com We want classic in the front and creative, colorfull at the back. The cards will be printed in relief, with very high quality of paper.
Industry/Entity Type
Insurance Broker
Colors
Designer to choose colors to be used in the design.
Look and feel

```html
<!DOCTYPE html>
<html lang="en">
<head>
<meta charset="utf-8">
<title>Tidewell Vantage – Business Card</title>
<link href="https://fonts.googleapis.com/css2?family=Montserrat:wght@600;700&family=Arimo:wght@400&display=swap" rel="stylesheet">
<style>
  :root {
    --stage: #1a1a1a;
    --card: #232223;
    --orange: #f26a21;
    --blue: #1e8fd5;
    --grey: #9a9a9a;
    --white: #f2f2f2;
  }
  * { box-sizing: border-box; margin: 0; padding: 0; }
  html, body {
    width: 1200px; height: 900px; overflow: hidden;
    background: var(--stage);
  }
  .canvas {
    width: 1200px; height: 900px;
    display: flex; flex-direction: column; align-items: center; justify-content: center;
    gap: 36px;
  }
  .card {
    position: relative;
    width: 700px; height: 400px;
    background: var(--card);
    overflow: hidden;
    box-shadow: 0 10px 30px rgba(0,0,0,.6);
  }
  .card__stripe {
    position: absolute; left: 0; right: 0; bottom: 0;
    height: 7px; background: var(--orange);
  }
  /* front */
  .brand {
    position: absolute; inset: 0 0 7px 0;
    display: flex; align-items: center; justify-content: center; gap: 16px;
  }
  .brand__dot {
    width: 34px; height: 34px; border-radius: 50%;
    background: var(--orange);
  }
  .brand__name {
    font-family: "Montserrat", sans-serif; font-weight: 700;
    font-size: 46px; letter-spacing: 1px; text-transform: uppercase;
    color: var(--blue);
  }
  /* back */
  .person {
    position: absolute; left: 150px; top: 150px; width: 210px; text-align: right;
  }
  .person__name {
    font-family: "Montserrat", sans-serif; font-weight: 700;
    font-size: 24px; line-height: 1; white-space: nowrap;
  }
  .person__first { color: var(--orange); }
  .person__last { color: var(--blue); }
  .person__role {
    font-family: "Arimo", sans-serif; font-size: 17px; color: var(--grey);
    margin-top: 2px;
  }
  .divider {
    position: absolute; left: 380px; top: 150px;
    width: 2px; height: 68px; background: var(--orange);
  }
  .contacts {
    position: absolute; left: 398px; top: 150px;
    list-style: none;
    font-family: "Arimo", sans-serif; font-size: 15px; color: var(--white);
  }
  .contacts__item {
    display: flex; align-items: center; gap: 10px; height: 24px;
  }
  .contacts__icon { width: 16px; height: 16px; flex: none; }
  .address {
    position: absolute; left: 0; right: 0; top: 318px; text-align: center;
    font-family: "Arimo", sans-serif; font-size: 16px; color: var(--white);
  }
</style>
</head>
<body>
<main class="canvas">
  <section class="card card--front">
    <div class="brand">
      <span class="brand__dot"></span>
      <span class="brand__name">Tidewell Vantage</span>
    </div>
    <div class="card__stripe"></div>
  </section>

  <section class="card card--back">
    <div class="person">
      <p class="person__name"><span class="person__first">Delton</span> <span class="person__last">Ashgrove</span></p>
      <p class="person__role">Managing Director</p>
    </div>
    <div class="divider"></div>
    <ul class="contacts">
      <li class="contacts__item">
        <svg class="contacts__icon" viewBox="0 0 24 24" aria-hidden="true"><path fill="#f26a21" d="M6.6 10.8a15 15 0 0 0 6.6 6.6l2.2-2.2c.3-.3.7-.4 1-.2 1.1.4 2.3.6 3.6.6.6 0 1 .4 1 1V20c0 .6-.4 1-1 1A17 17 0 0 1 3 4c0-.6.4-1 1-1h3.5c.6 0 1 .4 1 1 0 1.3.2 2.5.6 3.6.1.3 0 .7-.2 1z"/></svg>
        <span>Tel: (+244) 947 385 619</span>
      </li>
      <li class="contacts__item">
        <svg class="contacts__icon" viewBox="0 0 24 24" aria-hidden="true"><rect x="2" y="5" width="20" height="14" fill="none" stroke="#f26a21" stroke-width="2"/><path d="M2 5l10 8 10-8" fill="none" stroke="#f26a21" stroke-width="2"/></svg>
        <span>Email: delton.ashgrove@tidewell-v.com</span>
      </li>
      <li class="contacts__item">
        <svg class="contacts__icon" viewBox="0 0 24 24" aria-hidden="true"><g fill="none" stroke="#f26a21" stroke-width="2"><circle cx="12" cy="12" r="10"/><ellipse cx="12" cy="12" rx="4" ry="10"/><path d="M2 12h20M4 7h16M4 17h16"/></g></svg>
        <span>Website: www.tidewell-v. com</span>
      </li>
    </ul>
    <p class="address">N ° 73/74 Cmt. Bolembe - R / C 2B Esquerda - Bairro Quimbuta - Luanda</p>
    <div class="card__stripe"></div>
  </section>
</main>
</body>
</html>
```